Asset Mgmt Firm Business Card Design Project

We need a new business card design for our asset management firm. The name of the firm is Meridane CapiLeaf, and the firm is referred to as MCL. We would like to see designs that use blues and greys the business card is to be one-sided. The final design should be conservative to communicate financial safety and growth.

The card must include all of the elements below:

Dominick T. Halvorsen, PhD MBA
Founding Principal

Meridane CapiLeaf Inc
418 Fenwold Street
New York, NY 10482
212-804-3176
dthalvorsen@meridanecapileaf.example
www.meridanecapileaf.example

Our tagline:
"Placing the risk and reward for the future of biotechnology"

When designing the business card, please abide by Orlanto Press's guidelines here: http://www.orlantopress.example/op/ns/guide/UploadResources.aspx?selectedTab=0?pfid=088&pf_id=088&xnav=DocSpecs#Bleed

Please use Adobe Illustrator or Adobe Photoshop.

This project has now beenĀ guaranteed.

Best Regards,
Nick

Industry/Entity Type

Asset Management

Requirements
Must have
• logo

white background

```html
<!DOCTYPE html>
<html lang="en">
<head>
<meta charset="utf-8">
<title>Meridane CapiLeaf – Business Card</title>
<link rel="stylesheet" href="https://fonts.googleapis.com/css2?family=Cormorant+Garamond:ital,wght@0,500;1,500&family=Cormorant+SC:wght@500;700&display=swap">
<style>
  :root {
    --navy: #23225f;
    --helix-grey: #ececee;
    --card-white: #ffffff;
    --backdrop: #e6e6e8;
  }
  * { margin: 0; padding: 0; box-sizing: border-box; }
  html, body {
    width: 1200px; height: 849px; overflow: hidden;
    background: var(--backdrop);
  }
  .card {
    position: absolute; left: 88px; top: 133px;
    width: 1027px; height: 579px;
    background: var(--card-white);
    overflow: hidden;
    color: var(--navy);
  }
  .helix-decoration {
    position: absolute; left: 767px; top: 0;
    width: 260px; height: 579px;
    background: linear-gradient(90deg, rgba(236,236,238,0) 0%, var(--helix-grey) 35%, var(--helix-grey) 100%);
  }
  .arc-band { position: absolute; left: 0; top: 0; }
  .brand-name {
    position: absolute; left: 70px; top: 180px;
    width: 360px;
    font-family: "Cormorant Garamond", serif;
    font-weight: 500; font-size: 148px; line-height: 1;
    letter-spacing: 10px; white-space: nowrap;
    color: var(--navy);
  }
  .tagline {
    position: absolute; left: 77px; top: 355px;
    font-family: "Cormorant Garamond", serif;
    font-style: italic; font-weight: 500;
    font-size: 30px; line-height: 39px;
  }
  .identity, .contact {
    position: absolute; right: 46px; text-align: right;
    font-family: "Cormorant SC", serif; font-weight: 500;
  }
  .identity { top: 64px; }
  .identity .person-name { font-weight: 700; font-size: 26px; line-height: 32px; letter-spacing: 0.5px; }
  .identity .person-title { font-size: 21px; line-height: 26px; letter-spacing: 0.8px; }
  .contact { top: 364px; font-size: 22px; line-height: 29px; letter-spacing: 0.8px; }
  .contact .company { font-weight: 700; font-size: 20px; }
</style>
</head>
<body>
  <div class="card">
    <div class="helix-decoration" role="img" aria-label="Faint grey decorative helix pattern"></div>

    <svg class="arc-band" width="1027" height="579" viewBox="0 0 1027 579" aria-hidden="true">
      <path d="M367 0 L412 0 Q620 290 418 579 L365 579 Q575 290 367 0 Z" fill="var(--navy)"/>
    </svg>

    <div class="brand-name">MCL</div>

    <p class="tagline">Placing the risk and reward for<br>the future of biotechnology</p>

    <div class="identity">
      <div class="person-name">Dominick T. Halvorsen, PhD MBA</div>
      <div class="person-title">Founding Principal</div>
    </div>

    <div class="contact">
      <div class="company">meridane capileaf inc</div>
      <div>418 fenwold street</div>
      <div>new york, NY 10482</div>
      <div>212-804-3176</div>
      <div>dthalvorsen@meridanecapileaf.example</div>
      <div>www.meridanecapileaf.example</div>
    </div>
  </div>
</body>
</html>
```